Tidewell Cargo Links Website

We require a prominent webpage for a new concept on an old idea. We are a freight forwarding company in the Bahamas that will streamline the import process in the Bahamas for clients while offering both airfreight and seafreight import and export services . We would like the final design to communicate a professional image with stable service offering. Please view www.korvanfreight.example to see an example of what we require. Also view the site www.pemla.tariffgate.example and dorvelin.example. We will requier integration with these and other websites.

Target Market(s)

Small (<100) and medium (100-500) commercial businesses that require full importation services.

Industry/Entity Type

Freight Forwarding

Coding

Coded - Design and coding required

Number of Pages Required

5+ page

Colors

Designer to choose colors to be used in the design.

Requirements
Must have
• Core Website Development – Front End
• 1. Website Design
• 2. Coding and Development
• 4. Graphics
• 5. Social Media Integrations
• 6. Email Integration
• 7. Security / SSL Integrations
• 8. User Dashboard / Account
• 9. Customer Signup Integration
• 10. eCommerceOnlinePayment
• 11. XML–APIDevelopmentforDorvelin
• 12. DorvelinIntegrations

```html
<!DOCTYPE html>
<html lang="en">
<head>
<meta charset="utf-8">
<title>Tidewell Cargo Links</title>
<link href="https://fonts.googleapis.com/css2?family=Kaushan+Script&family=Open+Sans:wght@400;600;700&family=Roboto:wght@400;500;700;900&display=swap" rel="stylesheet">
<style>
:root{
  --red:#c8300f;
  --red-bright:#e1401c;
  --navy:#1f2358;
  --navy-deep:#1a2150;
  --indigo:#3d2f86;
  --charcoal:#3b3b3b;
  --footer:#333333;
  --footer-base:#262626;
  --ink:#222;
  --muted:#8a8a8a;
  --white:#fff;
  --cream:#fbf1ea;
}
*{margin:0;padding:0;box-sizing:border-box}
html,body{width:1200px;height:3169px;overflow:hidden;background:var(--white)}
body{position:relative;font-family:"Open Sans",Arial,sans-serif;color:var(--ink)}
.abs{position:absolute}
.script{font-family:"Kaushan Script",cursive;font-weight:400}

/* top bar & header */
.topbar{left:0;top:0;width:1200px;height:42px;background:var(--red-bright);color:#fff;font-size:14px;text-align:right;padding:12px 60px 0 0}
.brand{left:95px;top:14px;width:170px;height:140px;display:flex;flex-direction:column;align-items:center;justify-content:center;gap:8px;z-index:3}
.brand-dot{width:56px;height:56px;border-radius:50%;background:var(--navy)}
.brand-name{font-family:"Roboto",sans-serif;font-weight:700;font-size:17px;color:var(--navy);text-align:center;line-height:1.1}
.contact-item{top:76px;display:flex;gap:12px;align-items:flex-start}
.contact-item svg{width:22px;height:22px;margin-top:2px}
.contact-item b{display:block;font-family:"Roboto",sans-serif;font-weight:500;font-size:16px;color:#222}
.contact-item span{font-size:12px;color:#777}

/* nav */
.nav{left:93px;top:142px;width:1017px;height:46px;background:var(--navy);display:flex;align-items:center;z-index:2}
.nav a{font-family:"Roboto",sans-serif;font-weight:700;font-size:13px;color:#fff;text-decoration:none;padding:0 21px;height:46px;line-height:46px;position:relative}
.nav a.active::after{content:"";position:absolute;left:14px;right:14px;bottom:0;height:4px;background:var(--red-bright)}
.nav .inquiry{margin-left:auto;background:var(--cream);color:#111;padding:0 50px;height:42px;line-height:42px;margin-right:2px}

/* hero */
.hero{left:0;top:158px;width:1200px;height:502px;background:linear-gradient(160deg,#9fb4bf 0%,#6d8a98 35%,#3f5e6e 70%,#5d7785 100%)}
.hero-card{left:95px;top:290px;width:412px;height:165px;background:rgba(255,255,255,.86);padding:10px 12px}
.hero-card h1{font-size:50px;color:#111;line-height:1.1}
.hero-card p{font-size:12.5px;line-height:1.55;color:#222;margin-top:10px}

.service{top:560px;width:173px;height:296px}
.service .face{height:212px;background:var(--red);display:flex;flex-direction:column;align-items:center;justify-content:flex-end;padding-bottom:26px;color:#fff}
.service svg{width:74px;height:74px;margin-bottom:36px}
.service h3{font-family:"Roboto",sans-serif;font-weight:700;font-size:15.5px}
.service p{height:84px;background:var(--navy-deep);color:#dfe2f2;font-size:12px;line-height:1.35;text-align:center;padding:14px 12px}

.about-title{left:85px;top:695px;font-size:33px;color:#111}
.about-text{left:85px;top:748px;width:445px;font-size:12.5px;line-height:1.6;color:#222}

/* calculator */
.calc{left:0;top:997px;width:1200px;height:529px;background:var(--charcoal)}
.calc h2{position:absolute;left:85px;top:70px;font-size:38px;color:#fff}
.field-label{font-size:12.5px;color:#eee}
.input{background:#a8a8a8;border:2px solid #d0d0d0;height:33px;color:#e8e8e8;font-size:11px;padding:7px 12px;position:absolute}
.select::after{content:"";position:absolute;right:10px;top:13px;border:4px solid transparent;border-top-color:#555}
.calc .note{font-size:11px;color:#eee}
.calc-btn{left:415px;top:323px;width:112px;height:33px;background:var(--indigo);color:#fff;font-family:"Roboto",sans-serif;font-weight:700;font-size:12.5px;text-align:center;line-height:33px}
.worker{left:697px;top:76px;width:296px;height:453px;background:linear-gradient(180deg,#d9a98c 0%,#2c6fb8 30%,#1f5aa0 70%,#cdb8a0 100%);border-radius:120px 120px 0 0}

/* our services */
.services-title{left:68px;top:1680px;font-size:33px;color:#111}
.services-text{left:68px;top:1765px;width:505px;font-size:13px;line-height:1.7;color:var(--muted)}
.services-text p+p{margin-top:10px}
.video{left:608px;top:1646px;width:514px;height:342px;background:linear-gradient(135deg,#6e5a48 0%,#3a3f5a 45%,#1f2d6e 70%,#5a6070 100%)}
.play{left:214px;top:128px;width:86px;height:86px;border-radius:50%;background:#fff}

.banner{width:328px;color:#fff;padding:24px 22px}
.banner .num{font-family:"Roboto",sans-serif;font-size:30px;font-weight:500;opacity:.28;line-height:1}
.banner h4{font-family:"Roboto",sans-serif;font-weight:700;font-size:33px;line-height:1;margin-top:-4px}
.banner .sub{font-family:"Roboto",sans-serif;font-size:20px;color:#e39a2a;line-height:1.1}
.banner .more{font-family:"Roboto",sans-serif;font-weight:700;font-size:12px;margin-top:26px}
.banner .more::after{content:"";display:block;width:28px;height:2px;background:#fff;margin-top:12px}
.banner.navy{top:2092px;height:194px;background:linear-gradient(90deg,#3b2f78,#4a3f86)}
.banner.red{top:2064px;height:222px;background:var(--red-bright);padding-top:40px}
.banner.red .sub{color:#7a1b06}

/* testimonial */
.avatar{left:509px;top:2353px;width:94px;height:94px;border-radius:50%;background:linear-gradient(180deg,#c9a58e,#4a4f5a)}
.quote{left:90px;top:2470px;width:1020px;text-align:center;font-size:13.5px;line-height:1.6;color:var(--muted)}
.quote-mark{left:541px;top:2548px}
.person{left:0;top:2593px;width:1112px;text-align:center}
.person b{font-family:"Roboto",sans-serif;font-weight:700;font-size:23px;color:var(--indigo);display:block}
.person span{font-family:"Roboto",sans-serif;font-size:11px;font-weight:700;color:var(--red-bright)}
.dots{left:535px;top:2659px;display:flex;gap:8px}
.dots i{width:8px;height:8px;border-radius:50%;background:var(--navy)}
.dots i:last-child{background:var(--red-bright)}

/* footer */
.footer{left:0;top:2764px;width:1200px;height:363px;background:var(--footer)}
.callbar{left:0;top:2747px;width:560px;height:116px}
.callbar .txt{position:absolute;right:62px;top:12px;text-align:right;color:#fff}
.callbar small{font-size:19px;display:block}
.callbar b{font-family:"Open Sans",sans-serif;font-size:33px;font-weight:700;letter-spacing:.5px}
.stay{left:587px;top:2776px;font-size:21px;font-weight:700;color:#fff}
.f-input{top:2821px;height:34px;background:#fff;font-size:12.5px;color:#666;padding:8px 10px}
.submit{left:1008px;top:2821px;width:87px;height:34px;background:var(--red);color:#fff;font-weight:700;font-size:15px;text-align:center;line-height:34px}
.f-head{top:2920px;font-size:21px;font-weight:700;color:#fff}
.f-profile{left:101px;top:2968px;width:250px;font-size:12.5px;line-height:1.6;color:#eee}
.f-contact{left:418px;display:flex;gap:14px;font-size:11.5px;color:#eee;line-height:1.45}
.f-contact .ic{width:22px;height:22px;border-radius:50%;background:var(--red-bright);flex:none;display:flex;align-items:center;justify-content:center}
.f-links{left:693px;top:2962px;font-size:14px;color:#eee;line-height:27px;list-style:none}
.f-brand{left:883px;top:2893px;width:174px;height:150px;display:flex;flex-direction:column;align-items:center;justify-content:center;gap:8px}
.f-brand .brand-dot{background:#fff}
.f-brand .brand-name{color:#fff}
.socials{left:905px;top:3052px;display:flex;gap:17px}
.socials i{width:28px;height:28px;border-radius:50%;background:#2d8ad6}
.socials i:nth-child(2){background:#2aa3d8}
.socials i:nth-child(3){background:#e0561f}
.baseline{left:0;top:3127px;width:1200px;height:42px;background:var(--footer-base);color:#eee;font-size:13px;text-align:center;line-height:42px}
</style>
</head>
<body>

<div class="abs topbar">Now 547,684 packages we delivery to 8.903 stores</div>

<div class="abs hero" role="img" aria-label="Aerial photo of a loaded container ship sailing across the sea"></div>

<div class="abs brand">
  <div class="brand-dot"></div>
  <div class="brand-name">Tidewell Cargo Links</div>
</div>

<div class="abs contact-item" style="left:547px">
  <svg viewBox="0 0 24 24"><path fill="#c8300f" d="M6.6 10.8a15 15 0 0 0 6.6 6.6l2.2-2.2c.3-.3.7-.4 1-.2 1.1.4 2.3.6 3.6.6.6 0 1 .4 1 1V20c0 .6-.4 1-1 1A17 17 0 0 1 3 4c0-.6.4-1 1-1h3.5c.6 0 1 .4 1 1 0 1.3.2 2.5.6 3.6.1.3 0 .7-.2 1z"/></svg>
  <div><b>1-555-97-310</b><span>info@tidewellcargo.example</span></div>
</div>
<div class="abs contact-item" style="left:737px">
  <svg viewBox="0 0 24 24"><path fill="#c8300f" d="M12 3 2 12h3v8h5v-5h4v5h5v-8h3z"/></svg>
  <div><b>22 Harbour Lane</b><span>Nassau, Bahamas.</span></div>
</div>
<div class="abs contact-item" style="left:928px">
  <svg viewBox="0 0 24 24"><circle cx="12" cy="12" r="9" fill="none" stroke="#c8300f" stroke-width="2.5"/><path d="M12 7v5l3 2" stroke="#c8300f" stroke-width="2.2" fill="none"/></svg>
  <div><b>Mon - Sat : 9AM - 6PM</b><span>Opening Time</span></div>
</div>

<nav class="abs nav">
  <a class="active" style="margin-left:22px">HOME</a><a>FEATURES</a><a>SERVICES</a><a>ABOUT US</a><a>STORE</a><a>MEDIA</a><a>BLOG</a><a>CONTACT</a>
  <a class="inquiry">QUICK INQUIRY</a>
</nav>

<div class="abs hero-card">
  <h1 class="script">Freight Forwarding</h1>
  <p>company in the Bahamas that will streamline the import process in the Bahamas for clients while offering both airfreight and seafreight import and export services</p>
</div>

<div class="abs service" style="left:556px">
  <div class="face">
    <svg viewBox="0 0 64 64" fill="none" stroke="#fff" stroke-width="3"><path d="M8 38h48l-7 12H15z"/><rect x="18" y="26" width="28" height="12"/><rect x="26" y="14" width="12" height="12"/><path d="M6 56c6 3 10-3 16 0s10-3 16 0 10-3 16 0"/></svg>
    <h3>SEA SHIPPING</h3>
  </div>
  <p>We want to ensure that it's as easy as possible to use the site to get.</p>
</div>
<div class="abs service" style="left:742px">
  <div class="face">
    <svg viewBox="0 0 64 64" fill="none" stroke="#fff" stroke-width="3"><ellipse cx="32" cy="30" rx="8" ry="18"/><path d="M4 30h20M40 30h20M22 50h20M32 12v-6"/><circle cx="32" cy="28" r="3"/></svg>
    <h3>AIR SHIPPING</h3>
  </div>
  <p>Shipments moving, whether you've worked with us for years completely new.</p>
</div>
<div class="abs service" style="left:928px">
  <div class="face">
    <svg viewBox="0 0 64 64" fill="none" stroke="#fff" stroke-width="3"><rect x="8" y="10" width="18" height="16" transform="rotate(-15 17 18)"/><rect x="22" y="30" width="16" height="12"/><path d="M40 14v32h16M46 46l4-10h8"/><circle cx="44" cy="50" r="5"/><circle cx="58" cy="50" r="4"/></svg>
    <h3>LAND SHIPPING</h3>
  </div>
  <p>International shipping. For further assistance, please get in touch.</p>
</div>

<h2 class="abs about-title script">About Tidewell Cargo Links</h2>
<p class="abs about-text">Prominent service provider of complete portfolio of logistic services. We act as Custom House Agent and Custom Clearance Agent for Import and Export of goods. We take care of all the legal formalities associated with importing and exporting of goods. By being in the complete management of the solution, we aim to achieve a holistic balance in the complete loop of operations. We create value by operating from within the customer's existing networks and maximizing their potential.</p>

<section class="abs calc">
  <h2 class="script">Calculate Shipping</h2>
  <div class="abs field-label" style="left:91px;top:178px">Distance</div>
  <div class="input select" style="left:86px;top:198px;width:189px">foot</div>
  <div class="abs field-label" style="left:91px;top:233px">Weight</div>
  <div class="input" style="left:86px;top:253px;width:195px"></div>
  <div class="abs field-label" style="left:91px;top:303px">Cargo Size</div>
  <div class="input" style="left:86px;top:323px;width:60px">cm</div>
  <div class="abs field-label" style="left:155px;top:330px">x</div>
  <div class="input" style="left:170px;top:323px;width:60px">cm</div>
  <div class="abs field-label" style="left:91px;top:370px">Fragile</div>
  <div class="input select" style="left:86px;top:390px;width:189px">YES</div>
  <div class="abs field-label" style="left:415px;top:178px">Extra Services</div>
  <div class="input select" style="left:412px;top:198px;width:189px">foot</div>
  <div class="abs note" style="left:415px;top:244px">The Field below will show the double of the number about $</div>
  <div class="input" style="left:412px;top:274px;width:195px">0</div>
  <div class="abs calc-btn">CALCULATE</div>
  <div class="abs worker" role="img" aria-label="Photo of a delivery worker in a blue shirt holding a clipboard and a parcel"></div>
</section>

<h2 class="abs services-title script">Our Services</h2>
<div class="abs services-text">
  <p>Lorem ipsum dolor sit amet, consectetur adipiscing elit. Aenean finibus interdum urna.Phasellus ac lorem ut tellus ornare condimentum. Nulla facilisi. Nulla at facilisis nibh,in ultricies arcu. Fusce elementum mollis eros, vel ultricies enim consequat in.</p>
  <p>Proin diam turpis, semper vitae libero at, pulvinar eleifend lacus. Maecenas vel nisi dignissim, rutrum metus sit amet, facilisis enim. Maecenas quis elit viverra eros congue pulvinar eu et est. Nam commodo semper nunc non rem sit tellus ornare condimentum. Nulla facilisi. Nulla at facilisis nibh,in ultricies arcu..</p>
</div>
<div class="abs video" role="img" aria-label="Video still of parcels moving on warehouse conveyor rollers">
  <div class="abs play"></div>
  <svg class="abs" style="left:247px;top:152px" width="30" height="38" viewBox="0 0 30 38"><path d="M0 0 30 19 0 38z" fill="#111"/></svg>
</div>

<div class="abs banner navy" style="left:89px"><div class="num">01</div><h4>PACKING</h4><div class="sub">STORAGES</div><div class="more">READ MORE</div></div>
<div class="abs banner red" style="left:414px"><div class="num">02</div><h4>LANDING</h4><div class="sub">FEATURES</div><div class="more">READ MORE</div></div>
<div class="abs banner navy" style="left:742px"><div class="num">03</div><h4>DELIVERY</h4><div class="sub">SERVICES</div><div class="more">READ MORE</div></div>

<div class="abs avatar" role="img" aria-label="Portrait of the quoted senior marketing manager"></div>
<p class="abs quote">Our sea freight offering is complemented by our integrated warehousing and haulage services, which enable us to offer a true door-to-door service. As a company, we believe in operating as independent national carriers, this means we're able to offer you a global.</p>
<svg class="abs quote-mark" width="30" height="34" viewBox="0 0 30 34"><path d="M15 0a15 15 0 0 1 6 28.7L15 34l-3-5.3A15 15 0 0 1 15 0z" fill="#e1401c"/><text x="15" y="21" text-anchor="middle" font-family="Roboto,sans-serif" font-weight="900" font-size="18" fill="#fff">"</text></svg>
<div class="abs person"><b>Marcus Ellery</b><span>SENIOR MARKETTING</span></div>
<div class="abs dots"><i></i><i></i><i></i></div>

<footer class="abs footer"></footer>
<div class="abs callbar">
  <svg class="abs" width="560" height="116" viewBox="0 0 560 116"><path d="M0 0h560l-38 116H0z" fill="#c8300f"/></svg>
  <div class="txt"><small>You can call us toll free</small><b>1-800-555-0149</b></div>
</div>
<div class="abs stay">Stay in touch:</div>
<div class="abs f-input" style="left:587px;width:195px">Name</div>
<div class="abs f-input" style="left:799px;width:194px">Email</div>
<div class="abs submit">Submit</div>

<div class="abs f-head" style="left:101px">Company Profile</div>
<p class="abs f-profile">Corvana has been providing the radiation therapy community with innovative, quality and precise products for internal, external and brachytherapy products for over 30 years.</p>

<div class="abs f-head" style="left:418px">Contact Us</div>
<div class="abs f-contact" style="top:2968px">
  <span class="ic"><svg width="10" height="13" viewBox="0 0 10 13"><path d="M5 0a5 5 0 0 1 5 5c0 3.5-5 8-5 8S0 8.5 0 5a5 5 0 0 1 5-5z" fill="#fff"/><circle cx="5" cy="5" r="1.8" fill="#e1401c"/></svg></span>
  <div><b>QUAYLINE</b><br>780 Wharf Street,<br>Nassau, NP 10021</div>
</div>
<div class="abs f-contact" style="top:3032px">
  <span class="ic"><svg width="11" height="11" viewBox="0 0 24 24"><path fill="#fff" d="M6.6 10.8a15 15 0 0 0 6.6 6.6l2.2-2.2c.3-.3.7-.4 1-.2 1.1.4 2.3.6 3.6.6.6 0 1 .4 1 1V20c0 .6-.4 1-1 1A17 17 0 0 1 3 4c0-.6.4-1 1-1h3.5c.6 0 1 .4 1 1 0 1.3.2 2.5.6 3.6.1.3 0 .7-.2 1z"/></svg></span>
  <div style="padding-top:3px">1-800-555-0149</div>
</div>
<div class="abs f-contact" style="top:3072px">
  <span class="ic"><svg width="11" height="9" viewBox="0 0 11 9"><rect width="11" height="9" rx="1" fill="#fff"/><path d="M0 1l5.5 4L11 1" stroke="#e1401c" fill="none"/></svg></span>
  <div style="padding-top:3px">contact@quayline.example</div>
</div>

<div class="abs f-head" style="left:693px">Quick Links</div>
<ul class="abs f-links"><li>Services</li><li>Products</li><li>Projects</li><li>Team</li><li>Contact Us</li></ul>

<div class="abs f-brand">
  <div class="brand-dot"></div>
  <div class="brand-name">Tidewell Cargo Links</div>
</div>
<div class="abs socials"><i></i><i></i><i></i></div>

<div class="abs baseline">Tidewell Cargo Links All rights reserved. Copyright 2016-2017</div>

</body>
</html>
```